business card with 2 locations on 1 card

I need a modern looking business card that I would use at 2 different locations. Possibly 1 location on 1 side and other location on other side. One should be able to distinguish the 2 locations immediately before having to read the address or description on card. You can take a look at my website to see what I'm drawn to. The logo is brand new that I just purchased on Pixel Harbor. I want to emphasize family.
Updates

Let's not use the yellow and blue colors. Added Thursday, August 31, 2017

Target Market(s)

women and children

Industry/Entity Type

Health And Wellness

Contact Information for Business Card

Business name: Willow Nest Chiropractic & Acupuncture
My name: Delsa Brook
Job title: DC, MAOM, LAc (CA), CNS

Location 1
Address: 4817 Marlowe Blvd, Suite C-200, Frisco, TX 75036
Phone: (469) 555-0182
Fax: (972) 555-0147

Location 2
Address: 1786 Tenley Road, Suite 300, Plano, TX 75079
Phone: (469) 555-0195
Fax: (972) 555-0147

Email: drdelsabrook@mailvex.example
Website: www.drdelsabrook.example

Font styles to use
Serif
Sans Serif

Colors

Designer to choose colors to be used in the design.

Requirements
Must have
• distinction between 2 locations.
Nice to have
• Colors preference below is there. But I like to see what you come up with too!

```html
<!DOCTYPE html>
<html lang="en">
<head>
<meta charset="utf-8">
<title>Willow Nest Chiropractic &amp; Acupuncture — Business Card</title>
<link rel="stylesheet" href="https://fonts.googleapis.com/css2?family=Open+Sans:wght@400;700&display=swap">
<style>
  :root {
    --backdrop: #3b3431;
    --card: #141516;
    --card-edge: #1d1f20;
    --teal: #2f6f6d;
    --green: #3f9d4a;
    --ink: #e9eceb;
    --muted: #9fa5a4;
    --rule: #cfd3d2;
  }
  * { box-sizing: border-box; margin: 0; padding: 0; }
  html, body {
    width: 1200px; height: 864px; overflow: hidden;
    background: var(--backdrop);
  }
  .stage {
    position: relative; width: 1200px; height: 864px;
    display: flex; align-items: center; justify-content: center; gap: 40px;
  }
  .card {
    position: relative; width: 540px; height: 309px;
    background: var(--card);
    border: 1px solid var(--card-edge);
    box-shadow: 0 14px 30px rgba(0,0,0,.45);
    color: var(--ink);
    font-family: "Open Sans", Arial, sans-serif;
  }

  /* business name set in the card's own text font */
  .business {
    position: absolute; display: flex; align-items: center; gap: 12px;
    font-family: "Open Sans", Arial, sans-serif; font-weight: 700; color: var(--teal);
  }
  .business-dot {
    width: 14px; height: 14px; border-radius: 50%; background: var(--teal); flex: none;
  }
  .business-name { line-height: 1.15; }
  .business-name span { display: block; }
  .business-main { font-size: 30px; letter-spacing: .5px; }
  .business-sub { font-size: 12px; letter-spacing: .8px; text-transform: uppercase; }

  .card-front .business { left: 0; right: 0; top: 104px; justify-content: center; }
  .front-url {
    position: absolute; left: 0; right: 0; top: 248px; text-align: center;
    font-size: 13px; letter-spacing: 3px; color: var(--muted);
  }

  .card-back .business { left: 26px; width: 246px; top: 124px; gap: 10px; }
  .card-back .business-dot { width: 12px; height: 12px; }
  .card-back .business-main { font-size: 25px; }
  .card-back .business-sub { font-size: 10px; letter-spacing: .5px; }

  .divider {
    position: absolute; left: 282px; top: 34px; width: 1px; height: 240px;
    background: linear-gradient(to bottom, transparent, var(--rule) 30%, var(--rule) 70%, transparent);
  }
  .contact {
    position: absolute; left: 300px; top: 30px; right: 16px;
    font-size: 12.5px; line-height: 1.42;
  }
  .contact-name {
    font-weight: 700; font-size: 16px; letter-spacing: .5px; color: var(--teal);
    text-transform: uppercase; line-height: 1.1;
  }
  .contact-title { color: var(--green); font-size: 12.5px; margin-bottom: 6px; }
  .location { margin-bottom: 6px; }
  .line { display: flex; align-items: center; gap: 6px; white-space: nowrap; }
  .icon { width: 11px; height: 11px; flex: none; fill: var(--muted); }
  .web-lines { margin-top: 8px; }
</style>
</head>
<body>
<main class="stage">

  <section class="card card-front" aria-label="Card front">
    <div class="business">
      <div class="business-dot"></div>
      <p class="business-name">
        <span class="business-main">Willow Nest</span>
        <span class="business-sub">Chiropractic &amp; Acupuncture</span>
      </p>
    </div>
    <p class="front-url">www.drdelsabrook.example</p>
  </section>

  <section class="card card-back" aria-label="Card back">
    <div class="business">
      <div class="business-dot"></div>
      <p class="business-name">
        <span class="business-main">Willow Nest</span>
        <span class="business-sub">Chiropractic &amp; Acupuncture</span>
      </p>
    </div>
    <div class="divider"></div>
    <div class="contact">
      <p class="contact-name">Delsa Brook</p>
      <p class="contact-title">DC, MAOM, LAC (CA), CNS</p>

      <div class="location">
        <p>4817 Marlowe Blvd</p>
        <p>Suite C-200, Frisco, TX 75036</p>
        <p class="line"><svg class="icon" viewBox="0 0 12 12"><path d="M3 1h2l1 3-1.5 1a6 6 0 0 0 2.5 2.5L8 6l3 1v2a2 2 0 0 1-2 2A8 8 0 0 1 1 3a2 2 0 0 1 2-2z"/></svg>(469) 555-0182</p>
        <p class="line"><svg class="icon" viewBox="0 0 12 12"><rect x="3" y="1" width="6" height="3"/><rect x="1" y="5" width="10" height="6" rx="1"/></svg>(972) 555-0147</p>
      </div>

      <div class="location">
        <p>1786 Tenley Road</p>
        <p>Suite 300, Plano, TX 75079</p>
        <p class="line"><svg class="icon" viewBox="0 0 12 12"><path d="M3 1h2l1 3-1.5 1a6 6 0 0 0 2.5 2.5L8 6l3 1v2a2 2 0 0 1-2 2A8 8 0 0 1 1 3a2 2 0 0 1 2-2z"/></svg>(469) 555-0195</p>
        <p class="line"><svg class="icon" viewBox="0 0 12 12"><rect x="3" y="1" width="6" height="3"/><rect x="1" y="5" width="10" height="6" rx="1"/></svg>(972) 555-0147</p>
      </div>

      <div class="web-lines">
        <p class="line"><svg class="icon" viewBox="0 0 12 12"><rect x="1" y="2.5" width="10" height="7" rx="1"/></svg>drdelsabrook@mailvex.example</p>
        <p class="line"><svg class="icon" viewBox="0 0 12 12"><circle cx="6" cy="6" r="5"/></svg>www.drdelsabrook.example</p>
      </div>
    </div>
  </section>

</main>
</body>
</html>
```